Flyers

Modify Existing Flyer and create another for exterior company
Updates

Previous Brief has been updated- we want to update this existing one also

Target Market(s)

Exterior Remodeling Customers

Industry/Entity Type

Remodeling/Construction

```html
<!DOCTYPE html>
<html lang="en">
<head>
<meta charset="utf-8">
<title>Ridgeline Roofing and Exteriors – Flyer</title>
<link rel="stylesheet" href="https://fonts.googleapis.com/css2?family=Russo+One&family=Arimo:ital,wght@0,400;0,700;1,400&family=Didact+Gothic&family=Exo+2:wght@400;600&family=Passion+One:wght@700&display=swap">
<style>
  :root{
    --blue:#1274d6;
    --blue-deep:#0b5fbf;
    --orange:#f05a22;
    --black:#0a0a0a;
    --white:#ffffff;
    --ink:#1b1b1b;
    --quote:#d4e0f0;
  }
  *{margin:0;padding:0;box-sizing:border-box}
  html,body{width:960px;height:1200px;overflow:hidden;background:var(--white)}
  .flyer{position:relative;width:960px;height:1200px;overflow:hidden;background:var(--white);font-family:"Didact Gothic",sans-serif;color:var(--ink)}
  .abs{position:absolute}
  .hero-photo{left:0;top:0;width:960px;height:630px;background:linear-gradient(180deg,#3a7de0 0%,#7fb0ee 28%,#7d8ea6 52%,#5d6a80 100%)}
  .shapes{left:0;top:0;width:960px;height:1200px}
  .worker-photo{left:728px;top:285px;width:232px;height:322px;border-radius:60px 0 0 10px;background:linear-gradient(160deg,#c97a3a 0%,#6f7c90 35%,#b89a6c 70%,#8a6a3e 100%)}
  .brand{left:40px;top:0;width:334px;height:149px;background:var(--black);display:flex;flex-direction:column;align-items:center;justify-content:center;gap:8px}
  .brand-name{font-family:"Arimo",sans-serif;font-weight:700;color:var(--white);font-size:38px;letter-spacing:3px;line-height:1}
  .brand-sub{font-family:"Arimo",sans-serif;font-weight:700;color:var(--white);font-size:15.5px;letter-spacing:.5px;line-height:1;padding:6px 4px;border-top:2px solid var(--blue);border-bottom:2px solid var(--blue)}
  .headline{left:520px;top:44px;width:366px;text-align:center;font-family:"Russo One",sans-serif;font-size:34px;line-height:40px;letter-spacing:-1px}
  .headline .light{color:var(--white)}
  .headline .dark{color:var(--black)}
  .inset-photo{left:54px;top:527px;width:363px;height:252px;border:1px solid #333;background:linear-gradient(180deg,#8da6d8 0%,#b6c4dc 35%,#8c8778 60%,#4f8a2c 82%,#3f7a22 100%)}
  .section-title{left:438px;top:527px;width:290px;height:81px;background:var(--blue);color:var(--white);font-family:"Arimo",sans-serif;font-weight:700;font-size:30px;line-height:31px;padding:13px 0 0 15px}
  .tagline{left:452px;top:620px;font-family:"Arimo",sans-serif;font-style:italic;color:var(--orange);font-size:23.5px}
  .copy{font-size:17px;line-height:20px;text-align:justify;color:var(--ink)}
  .copy-a{left:450px;top:664px;width:463px}
  .copy-b{left:57px;top:790px;width:618px}
  .quote-mark{font-family:"Passion One",sans-serif;color:var(--quote);font-size:260px;line-height:1}
  .quote-open{left:10px;top:872px}
  .quote-close{left:300px;top:1058px}
  .services{left:0;top:889px;width:960px;height:49px;background:var(--orange);display:flex;align-items:center;padding-left:44px;list-style:none;font-family:"Arimo",sans-serif;font-weight:700;color:var(--white);font-size:22px}
  .service{display:flex;align-items:center;gap:16px;margin-right:21px}
  .service svg{width:38px;height:38px;stroke:var(--white);fill:none;stroke-width:1.6}
  .reviews-title{left:109px;top:975px;font-family:"Arimo",sans-serif;font-weight:700;color:var(--blue);font-size:24px}
  .review{left:58px;top:1018px;width:380px;text-align:center;font-size:16px;line-height:19.5px;color:var(--ink)}
  .reviewer{left:58px;top:1132px;width:380px;text-align:center;font-family:"Arimo",sans-serif;font-weight:700;color:var(--orange);font-size:14.5px}
  .contact-panel{left:0;top:0;width:960px;height:1200px}
  .contact{left:580px;top:953px;width:360px;text-align:center;color:var(--white)}
  .contact-ask{font-family:"Arimo",sans-serif;font-weight:700;font-size:24px;line-height:21px;letter-spacing:-.5px}
  .contact-note{font-family:"Arimo",sans-serif;font-style:italic;font-size:16.5px;line-height:20px;margin-top:8px}
  .rule{width:122px;height:2px;background:var(--orange);margin:9px auto}
  .phone{font-family:"Exo 2",sans-serif;font-weight:600;font-size:40px;line-height:38px}
  .web{font-family:"Exo 2",sans-serif;font-weight:400;font-size:25.5px;line-height:28px;letter-spacing:.5px}
  .address{font-family:"Exo 2",sans-serif;font-size:17.5px;line-height:23px}
</style>
</head>
<body>
<main class="flyer">
  <div class="abs hero-photo" role="img" aria-label="Photo of a house roof with grey asphalt shingles, brick chimneys and blue trim under a blue sky with clouds"></div>

  <svg class="abs shapes" viewBox="0 0 960 1200" aria-hidden="true">
    <polygon points="0,548 442,391 960,568 960,626 442,432" fill="var(--orange)"/>
    <polygon points="0,548 442,432 960,626 960,1200 0,1200" fill="var(--white)"/>
    <polygon points="774,787 883,886 848,886 774,820 700,886 671,886" fill="var(--orange)"/>
    <polygon points="774,826 841,886 705,886" fill="var(--blue)"/>
    <g fill="var(--white)">
      <rect x="764" y="853" width="8" height="8"/><rect x="774" y="853" width="8" height="8"/>
      <rect x="764" y="863" width="8" height="8"/><rect x="774" y="863" width="8" height="8"/>
    </g>
  </svg>

  <div class="abs worker-photo" role="img" aria-label="Photo of a roofer in a cap, plaid shirt and work boots kneeling on the roof"></div>

  <div class="abs brand">
    <span class="brand-name">RIDGELINE</span>
    <span class="brand-sub">ROOFING AND EXTERIORS</span>
  </div>

  <h1 class="abs headline">
    <span class="light">BOOST YOUR<br>PROPERTY VALUE</span><br>
    <span class="dark">WITH A BRAND<br>NEW ROOF</span>
  </h1>

  <div class="abs inset-photo" role="img" aria-label="Photo of a two-storey grey-sided house with a stone chimney and green lawn"></div>

  <h2 class="abs section-title">TRANSFORM<br>YOUR EXTERIOR</h2>
  <p class="abs tagline">We install new decks, siding &amp; roofs</p>

  <p class="abs copy copy-a">If you want to increase your property value, updating your exterior is a great option. The team at Ridgeline Roofing &amp; Exteriors has over 25 years of experience installing and repairing roofs, so you can count on us to do an amazing job.</p>
  <p class="abs copy copy-b">Along with being experienced roofers, we're also extremely skilled deck and siding installers. You can add an exciting outdoor entertainment area to your property with a brand-new deck from us. Depend on us to take on your exterior improvement job in the Ankeny, IA area.</p>

  <span class="abs quote-mark quote-open" aria-hidden="true">“</span>
  <span class="abs quote-mark quote-close" aria-hidden="true">”</span>

  <ul class="abs services">
    <li class="service">
      <svg viewBox="0 0 38 38"><path d="M4 17 19 5l15 12"/><path d="M8 14v19h22V14"/><rect x="13" y="19" width="12" height="10"/><path d="M19 19v10M13 24h12"/></svg>SIDING
    </li>
    <li class="service">
      <svg viewBox="0 0 38 38"><rect x="5" y="5" width="28" height="28"/><path d="M11 5v28M17 5v28M23 5v28M29 5v28M5 13h6M17 20h6M11 27h6M23 11h6"/></svg>DECKING
    </li>
    <li class="service">
      <svg viewBox="0 0 38 38"><path d="M10 10h18l8 20H2z"/><path d="M14 10 11 30M19 10v20M24 10l3 20M6 20h26M4 25h30"/></svg>METAL ROOFING
    </li>
    <li class="service">
      <svg viewBox="0 0 38 38"><path d="M3 19 17 6l6 6 3-5 2 7 6 5"/><path d="M7 16v17h24V16"/><rect x="15" y="23" width="8" height="10"/><path d="M20 9l-3 6 4 2-2 5"/></svg>STORM DAMAGE
    </li>
  </ul>

  <h3 class="abs reviews-title">CUSTOMER REVIEWS</h3>
  <p class="abs review">What a beatutiful kitchen! We hired Ridgeline Roofing - they truly are a wonderful company to workwith. From our first meeting until the last day we enjoyed all the workers in our home. Great local company !</p>
  <p class="abs reviewer">Marcus T.</p>

  <svg class="abs contact-panel" viewBox="0 0 960 1200" aria-hidden="true">
    <polygon points="628,941 904,941 960,990 960,1200 353,1200" fill="var(--blue)"/>
    <line x1="616" y1="941" x2="506" y2="1043" stroke="var(--orange)" stroke-width="3"/>
    <polygon points="918,941 940,941 960,958 960,978" fill="var(--orange)"/>
  </svg>

  <section class="abs contact">
    <p class="contact-ask">NEED ROOF<br>REPAIR SERVICES?</p>
    <p class="contact-note">Contact a local roofing company<br>serving the Des Moines area</p>
    <div class="rule"></div>
    <p class="phone">(515) 555-0142</p>
    <p class="web">RIDGELINEROOFIA.COM</p>
    <div class="rule"></div>
    <p class="address">48 Cedar Hollow Road<br>Suite 210, Ankeny, IA 50021</p>
  </section>
</main>
</body>
</html>
```